Business Card Design Project

TRK Solutions is a Electrical and Communications Services and Maintenance contractor to the Mining Oil and Gas sectors of Australia.
Our clients will be planners, Schedulers, Tradespeople and Engineers

We are yet to determine the primary colours that we will use on the business cards but the logos attached will form foundation of the colours used for logos on Business cards, Website, Uniforms, vehicles etc.

Target Market(s)

Mining engineers and shedulers

Industry/Entity Type

Contractor

Requirements
Must have
• information to be included on the card

Name: Derek Hanley
Title: Managing Director
Company: TRK Solutions Pty Ltd
Phone: 08 9YYY YYYY
Mobile 0400 813 942
email: dhanley@trksolutions-example.com
Website www.trksolutions-example.com

Address: U5/7 Bexley Street Ravensford, WA 6127
Postal Address: PO Box 4187 Ravensford WA 6129

Nice to have
• Double sided. Maybe the logo on the back

```html
<!DOCTYPE html>
<html lang="en">
<head>
<meta charset="utf-8">
<title>TRK Solutions – Business Card</title>
<link rel="stylesheet" href="https://fonts.googleapis.com/css2?family=Titillium+Web:wght@400;600&display=swap">
<style>
  :root {
    --page-bg: #d9d9d9;
    --card-bg: #2e2e2e;
    --card-edge: #3a3a3a;
    --text-light: #f2f2f2;
    --text-muted: #cfcfcf;
    --accent: #f07a22;
    --divider: #8a8a8a;
  }
  * { box-sizing: border-box; margin: 0; padding: 0; }
  html, body {
    width: 928px;
    height: 1200px;
    overflow: hidden;
    background: var(--page-bg);
    font-family: "Titillium Web", Arial, sans-serif;
  }
  .sheet {
    position: relative;
    width: 928px;
    height: 1200px;
  }
  .card {
    position: absolute;
    left: 154px;
    width: 620px;
    height: 352px;
    border-radius: 34px;
    background: var(--card-bg);
    border: 1px solid var(--card-edge);
    box-shadow: 0 10px 24px rgba(0,0,0,0.25);
    color: var(--text-light);
  }
  .card--front { top: 200px; }
  .card--back  { top: 640px; }

  .brand {
    position: absolute;
    left: 80px;
    top: 92px;
    display: flex;
    align-items: center;
    gap: 16px;
  }
  .brand__mark {
    width: 22px;
    height: 22px;
    background: var(--accent);
  }
  .brand__name {
    font-size: 46px;
    font-weight: 600;
    letter-spacing: 1px;
    color: var(--text-light);
    line-height: 1;
  }

  .contact {
    position: absolute;
    right: 60px;
    bottom: 48px;
    display: flex;
    align-items: stretch;
  }
  .contact__person {
    text-align: right;
    padding-right: 16px;
    border-right: 1px solid var(--divider);
    display: flex;
    flex-direction: column;
    justify-content: flex-end;
    font-size: 12px;
    line-height: 1.45;
  }
  .contact__name { font-weight: 600; }
  .contact__role { color: var(--text-muted); }
  .contact__details {
    padding-left: 16px;
    font-size: 12px;
    line-height: 1.45;
    color: var(--text-muted);
  }
  .contact__company { font-weight: 600; color: var(--text-light); }
  .contact__label { font-weight: 600; color: var(--text-light); }
  .contact__web {
    color: var(--accent);
    letter-spacing: 1.5px;
  }

  .address {
    position: absolute;
    right: 60px;
    bottom: 56px;
    font-size: 13px;
    line-height: 1.45;
    color: var(--text-muted);
    text-align: left;
  }
</style>
</head>
<body>
<main class="sheet">
  <section class="card card--front" aria-label="Card front">
    <div class="brand">
      <span class="brand__mark"></span>
      <span class="brand__name">TRK Solutions</span>
    </div>
    <div class="contact">
      <div class="contact__person">
        <span class="contact__name">Derek Hanley</span>
        <span class="contact__role">Managing Director</span>
      </div>
      <div class="contact__details">
        <div class="contact__company">TRK Solutions Pty Ltd</div>
        <div><span class="contact__label">P</span> 08 9YYY YYYY&nbsp;&nbsp;<span class="contact__label">M</span> 0400 813 942</div>
        <div>dhanley@trksolutions-example.com</div>
        <div class="contact__web">www.trksolutions-example.com</div>
      </div>
    </div>
  </section>

  <section class="card card--back" aria-label="Card back">
    <div class="brand">
      <span class="brand__mark"></span>
      <span class="brand__name">TRK Solutions</span>
    </div>
    <div class="address">
      <div>Address: U5/7 Bexley Street Ravensford, WA 6127</div>
      <div>Postal Address: PO Box 4187 Ravensford WA 6129</div>
    </div>
  </section>
</main>
</body>
</html>
```